Fresh Business Card Designs Required

Looking to get new business cards but want a fresh look and feel. The logo has a large curved square which can be incorporated, or alternative the text-only version of the logo can be utilised if it is better. Looking for fresh ideas. I prefer flat designs, also incorporating a QR code to our contact us page on website would be great to make contact easy.
Updates

I have just uploaded the .ai files for our logo to make it easier to drop into your designs. Thanks for your consideration looking forward to seeing the results!

Target Market(s)

Generally business cards are handed to consumers who are contacting us for information.

Industry/Entity Type

Water Pumping and Irrigation, Water Filtration,

Contact Information for Business Card

Company Name / Logo, Name, Job Title, Phone No., 02 5550 1848, 14 Harbour Road, Eastbay NSW 2450

Font styles to use
Sans Serif

Colors
00AB8E
00BBA5
67D7C9
C6EFE9
E9F9F6
FFF300
FFF600
FEFA6F
FFFEC7
FFFEE8

Requirements
Must have
• Contact Details!!!! :)
Nice to have
• QR Code to contact us page, list of products (not critical!)

```html
<!DOCTYPE html>
<html lang="en">
<head>
<meta charset="utf-8">
<title>Eastern Bay Power &amp; Water – Business Card</title>
<link rel="stylesheet" href="https://fonts.googleapis.com/css2?family=Fira+Sans+Condensed:wght@500;600&display=swap">
<style>
  :root {
    --page: #ffffff;
    --card-centre: #eff217;
    --card-mid: #e2e519;
    --card-edge: #c7c917;
    --ink-green: #1e6b0c;
    --qr-fill: #1e6b0c;
    --qr-ground: #fffee8;
    --card-radius: 66px;
  }

  * { margin: 0; padding: 0; box-sizing: border-box; }

  html, body {
    width: 1200px;
    height: 686px;
    overflow: hidden;
    background: var(--page);
  }

  .card {
    position: relative;
    width: 1200px;
    height: 686px;
    border-radius: var(--card-radius);
    background: radial-gradient(ellipse 60% 75% at 50% 50%,
      var(--card-centre) 0%, var(--card-mid) 55%, var(--card-edge) 100%);
    font-family: "Fira Sans Condensed", "Arial Narrow", sans-serif;
    font-weight: 600;
    color: var(--ink-green);
    text-transform: uppercase;
    text-align: center;
  }

  .company-name {
    position: absolute;
    top: 166px;
    left: 0;
    width: 100%;
    font-size: 49px;
    font-weight: 600;
    line-height: 1;
    letter-spacing: 1px;
  }

  .tagline {
    position: absolute;
    top: 260px;
    left: 0;
    width: 100%;
    font-size: 35px;
    line-height: 1;
    letter-spacing: 5px;
    word-spacing: 34px;
  }

  .product-list {
    position: absolute;
    top: 364px;
    left: 0;
    width: 100%;
    list-style: none;
    font-size: 31px;
    line-height: 43px;
    letter-spacing: 5px;
  }

  .product-list li::before {
    content: "•";
    margin-right: 10px;
  }

  .contact {
    position: absolute;
    top: 604px;
    left: 0;
    width: 100%;
    font-size: 19px;
    font-weight: 500;
    line-height: 26px;
    letter-spacing: 1.5px;
    font-style: normal;
  }

  .contact-name { font-weight: 600; }

  .qr-code {
    position: absolute;
    top: 520px;
    left: 1050px;
    width: 96px;
    height: 96px;
  }
</style>
</head>
<body>
  <div class="card">
    <h1 class="company-name">Eastern Bay Power &amp; Water</h1>
    <p class="tagline">Sales / Service / Repairs</p>
    <ul class="product-list">
      <li>Solar Power Systems</li>
      <li>Hot Water Systems</li>
      <li>Energy Storage / Solar Pumping</li>
      <li>Generators / Irrigation</li>
      <li>Filtration / Pumps / Tanks</li>
    </ul>
    <address class="contact">
      <span class="contact-name">Jordan Reeve</span> · Sales Manager · Ph 02 5550 1847 · Direct 02 5550 1848<br>
      14 Harbour Road, Eastbay NSW 2450
    </address>
    <svg class="qr-code" viewBox="0 0 96 96" role="img" aria-label="QR code linking to the contact us page">
      <rect x="0" y="0" width="96" height="96" rx="6" fill="var(--qr-ground)"/>
      <rect x="10" y="10" width="76" height="76" rx="3" fill="var(--qr-fill)" opacity="0.85"/>
    </svg>
  </div>
</body>
</html>
```